2018 Brontor 3400 Velto construction

Eye catching and progressional design needed, not too busy, must integrate website, phone and our logo. We would like a complete wrap design covering the entire truck. I have a 2018 brontor 3400 crew cab. I am open to designs. Really want people to notice the company vehicle and remember the name and logo.

Target Market(s)

Middle class-to- high end clients

Industry/Entity Type

Construction

Font styles to use
Other font styles liked:
• Montserrat

Colors

Designer to choose colors to be used in the design.

Requirements
Must have
• Phone number: 555-417-2868 Website: Veltoconstruction.example Licensed and insured
Nice to have
• Bathrooms, kitchens, additions, new construction, remodeling

```html
<!DOCTYPE html>
<html lang="en">
<head>
<meta charset="utf-8">
<title>Velto Construction – Vehicle Wrap</title>
<link href="https://fonts.googleapis.com/css2?family=Montserrat:wght@400;500;600;700&display=swap" rel="stylesheet">
<style>
  :root {
    --page: #f2f2f2;
    --copper-light: #b0602a;
    --copper: #8e4418;
    --copper-dark: #5e2a0e;
    --steel: #8d9096;
    --steel-dark: #6e7177;
    --band: #5a1e10;
    --ink-light: #e9e2dc;
    --ink-dark: #2a2a2c;
  }
  * { margin: 0; padding: 0; box-sizing: border-box; }
  html, body { width: 1200px; height: 1200px; overflow: hidden; }
  body {
    background: var(--page);
    font-family: "Montserrat", sans-serif;
    position: relative;
  }
  .wrap-panel {
    position: absolute;
    left: 50px; top: 390px;
    width: 1100px; height: 420px;
    background: linear-gradient(180deg, var(--copper-light) 0%, var(--copper) 55%, var(--copper-dark) 100%);
    border-radius: 6px;
    overflow: hidden;
  }
  .door-panel {
    position: absolute;
    left: 75px; top: 110px;
    width: 220px; height: 220px;
    background: linear-gradient(180deg, var(--steel) 0%, var(--steel-dark) 100%);
    display: flex; align-items: center; justify-content: center;
  }
  .brand-name {
    color: var(--ink-dark);
    font-weight: 600;
    font-size: 19px;
    line-height: 1.2;
    text-align: center;
  }
  .services {
    position: absolute;
    left: 318px; top: 112px;
    list-style: none;
    color: var(--ink-light);
    font-weight: 500;
    font-size: 20px;
    line-height: 1.22;
  }
  .phone-band {
    position: absolute;
    left: 592px; top: 145px;
    width: 230px; height: 46px;
    background: var(--band);
    color: #fff;
    font-weight: 700;
    font-size: 23px;
    letter-spacing: 0.02em;
    display: flex; align-items: center; justify-content: center;
  }
  .contact {
    position: absolute;
    left: 836px; top: 142px;
    color: var(--ink-light);
    font-weight: 400;
    font-size: 18px;
    line-height: 1.25;
    opacity: 0.85;
  }
</style>
</head>
<body>
  <section class="wrap-panel" aria-label="Velto Construction vehicle wrap side layout">
    <div class="door-panel">
      <p class="brand-name">Velto construction</p>
    </div>
    <ul class="services">
      <li>Bathrooms</li>
      <li>Kitchens</li>
      <li>Additions</li>
      <li>New construction</li>
      <li>Remodeling</li>
    </ul>
    <div class="phone-band">555-417-2868</div>
    <div class="contact">
      <p>Veltoconstruction.example</p>
      <p>Licensed and insured</p>
    </div>
  </section>
</body>
</html>
```